Video Production Company Website

A video production company website for "Quiet Fern Studios"
Home page must have video player and way to select between 3 different videos.

Company does video Post production : Editing, Motion Graphics, Color correction, and Aerial videography

Design should be simple but Pro looking..

Earthy color palette with slight texture..

Industry/Entity Type

Film Production

Number of Pages Required

3 page

Font styles to use
Sans Serif
Other font styles liked:

Requirements
Nice to have
• Thumbnails on homepage to past project clips
Should not have
• full page video

```html
<!DOCTYPE html>
<html lang="en">
<head>
<meta charset="utf-8">
<title>Quiet Fern Studios — Video Post Production</title>
<link href="https://fonts.googleapis.com/css2?family=Oswald:wght@400;600&family=Open+Sans:wght@300;400;600;700&display=swap" rel="stylesheet">
<style>
  :root {
    --ink: #2a2520;
    --ink-soft: #3a332c;
    --gold: #e9b744;
    --sand: #f2cd6c;
    --sand-deep: #e6bb52;
    --paper: #ffffff;
    --text: #555049;
    --muted: #8a847c;
    --accent: #d9534f;
    --hero-top: #1f3547;
    --hero-mid: #4b6f8a;
    --hero-low: #7f8fa0;
  }
  * { margin: 0; padding: 0; box-sizing: border-box; }
  html, body { width: 763px; height: 1200px; overflow: hidden; }
  body {
    position: relative;
    background: var(--paper);
    font-family: "Open Sans", Arial, sans-serif;
    color: var(--text);
  }

  /* Hero */
  .hero {
    position: absolute; left: 0; top: 0; width: 763px; height: 384px;
    background:
      radial-gradient(ellipse at 72% 40%, rgba(230,225,215,.55), transparent 55%),
      linear-gradient(160deg, var(--hero-top) 0%, var(--hero-mid) 55%, var(--hero-low) 100%);
  }
  .hero-headline {
    position: absolute; left: 224px; top: 150px;
    font-family: "Oswald", Arial, sans-serif; color: #fff; font-weight: 600;
    font-size: 30px; line-height: 1.05; letter-spacing: .5px;
  }
  .hero-headline span { display: block; font-size: 34px; letter-spacing: 1.5px; }
  .hero-copy {
    position: absolute; left: 224px; top: 232px; width: 200px;
    font-size: 8px; line-height: 1.5; color: #e6edf3;
  }
  .slider-controls { position: absolute; left: 228px; top: 300px; display: flex; gap: 8px; }
  .slider-controls span {
    width: 22px; height: 22px; border-radius: 50%; border: 1.5px solid #fff;
    display: flex; align-items: center; justify-content: center;
  }

  /* Sidebar */
  .sidebar {
    position: absolute; left: 63px; top: 0; width: 134px; height: 268px;
    background: var(--ink);
  }
  .brand {
    height: 96px; background: var(--gold);
    display: flex; align-items: center; justify-content: center;
    font-family: "Oswald", Arial, sans-serif; font-weight: 600; font-size: 20px; color: var(--ink);
  }
  .nav { list-style: none; padding-top: 6px; }
  .nav li {
    display: flex; align-items: center; gap: 8px;
    height: 27px; padding-left: 14px;
    font-size: 9px; color: #eee;
  }
  .nav li.active { background: var(--gold); color: var(--ink); margin-top: -6px; margin-bottom: 4px; }
  .nav li i { width: 8px; height: 8px; border-radius: 50%; border: 1.5px solid currentColor; display: block; }

  /* Services */
  .services {
    position: absolute; left: 0; top: 384px; width: 763px; height: 208px;
    background:
      repeating-linear-gradient(45deg, rgba(255,255,255,.06) 0 2px, transparent 2px 6px),
      linear-gradient(180deg, var(--sand) 0%, var(--sand-deep) 100%);
  }
  .services-tab {
    position: absolute; left: 228px; top: 0; width: 307px; height: 24px;
    background: var(--ink); color: #fff;
    font-family: "Oswald", Arial, sans-serif; font-size: 11px; letter-spacing: 1px;
    display: flex; align-items: center; justify-content: center;
  }
  .service {
    position: absolute; top: 50px; width: 180px; text-align: center;
  }
  .service-icon {
    width: 50px; height: 50px; margin: 0 auto; border-radius: 50%;
    background: var(--ink); display: flex; align-items: center; justify-content: center;
  }
  .service h3 {
    font-family: "Open Sans", Arial, sans-serif; font-weight: 700; font-size: 9px;
    color: var(--ink); margin-top: 20px; letter-spacing: .5px;
  }
  .service p { font-size: 7px; line-height: 1.5; margin-top: 6px; color: #5a4a30; }

  /* Past projects */
  .section-title {
    position: absolute; left: 0; width: 763px; text-align: center;
    font-weight: 300; font-size: 24px; color: #3a3a3a;
  }
  .section-intro {
    position: absolute; left: 70px; width: 623px; text-align: center;
    font-size: 7px; line-height: 1.6; color: var(--muted);
  }
  .project { position: absolute; top: 714px; width: 202px; }
  .project-thumb {
    height: 136px; position: relative;
    display: flex; align-items: center; justify-content: center;
  }
  .project-thumb .play {
    width: 30px; height: 30px; border-radius: 50%; background: rgba(0,0,0,.45);
    display: flex; align-items: center; justify-content: center;
  }
  .thumb-warm { background: linear-gradient(135deg, #c9a27a, #6f5a48 70%, #3c3028); }
  .thumb-green { background: linear-gradient(135deg, #7a8a58, #5a6a4a 60%, #3a4030); }
  .thumb-blue { background: linear-gradient(135deg, #1b3f78, #3e7cc0 60%, #9bb9d8); }
  .project h4 { font-size: 8px; font-weight: 700; color: #444; margin-top: 10px; }
  .project p { font-size: 7px; line-height: 1.5; color: var(--muted); margin-top: 4px; width: 160px; }
  .project .more {
    position: absolute; right: 0; top: 172px; width: 16px; height: 16px; border-radius: 50%;
    border: 1.5px solid var(--accent); display: flex; align-items: center; justify-content: center;
  }

  .divider { position: absolute; top: 940px; left: 63px; width: 637px; height: 1px; background: #ddd; }
  .divider::after {
    content: ""; position: absolute; left: 314px; top: -4px; width: 8px; height: 8px;
    border-radius: 50%; background: #fff; border: 1px solid #ccc;
  }

  .read-more {
    position: absolute; left: 345px; top: 1072px; width: 72px; height: 20px;
    border: 1px solid #bbb; font-size: 7px; font-weight: 700; color: #444;
    display: flex; align-items: center; justify-content: center; gap: 4px;
  }

  /* Footer */
  .footer {
    position: absolute; left: 0; top: 1118px; width: 763px; height: 82px;
    background: var(--ink); color: #bdb6ad;
  }
  .footer-col { position: absolute; top: 28px; font-size: 7px; line-height: 1.5; }
  .footer-col strong { display: block; font-size: 9px; color: #fff; font-weight: 600; letter-spacing: .5px; }
  .follow { position: absolute; right: 63px; top: 30px; display: flex; align-items: center; gap: 5px; font-size: 9px; color: #fff; }
  .follow span.label { margin-right: 4px; letter-spacing: .5px; }
  .follow i { display: block; width: 13px; height: 13px; background: #8f877d; }
</style>
</head>
<body>

<header class="hero" role="img" aria-label="Photo of a vintage film projector beaming light in a dusky blue room">
</header>

<nav class="sidebar">
  <div class="brand">QuietFern</div>
  <ul class="nav">
    <li class="active"><i></i>Home</li>
    <li><i></i>About Quiet Fern</li>
    <li><i></i>Video Production</li>
    <li><i></i>Past Projects</li>
    <li><i></i>Contact Us</li>
  </ul>
</nav>

<h1 class="hero-headline">QuietFern<span>STUDIOS</span></h1>
<p class="hero-copy">Lorem ipsum dolor sit amet, consectetur adipiscing elit, sed do eiusmod tempor incididunt ut labore et dolore magna.</p>
<div class="slider-controls">
  <span><svg width="8" height="8" viewBox="0 0 8 8"><path d="M5.5 1 2.5 4l3 3" fill="none" stroke="#fff" stroke-width="1.4"/></svg></span>
  <span><svg width="8" height="8" viewBox="0 0 8 8"><path d="M2.5 1 5.5 4l-3 3" fill="none" stroke="#fff" stroke-width="1.4"/></svg></span>
</div>

<section class="services">
  <div class="services-tab">VIDEO POST PRODUCTION</div>

  <div class="service" style="left:63px;">
    <div class="service-icon">
      <svg width="22" height="20" viewBox="0 0 22 20"><rect x="1" y="1" width="20" height="13" rx="1" fill="none" stroke="#fff" stroke-width="1.6"/><path d="M8 18h6M11 14v4" stroke="#fff" stroke-width="1.6"/></svg>
    </div>
    <h3>EDITING</h3>
    <p>Lorem ipsum dolor sit amet, consectetur adipiscing elit, sed do eiusmod tempor incididunt ut labore et dolore magna aliqua.</p>
  </div>

  <div class="service" style="left:291px;">
    <div class="service-icon">
      <svg width="22" height="22" viewBox="0 0 22 22"><circle cx="11" cy="11" r="9" fill="none" stroke="#fff" stroke-width="1.6"/><circle cx="11" cy="11" r="4" fill="none" stroke="#fff" stroke-width="1.6"/><circle cx="11" cy="11" r="1.2" fill="#fff"/></svg>
    </div>
    <h3>MOTION GRAPHICS</h3>
    <p>Lorem ipsum dolor sit amet, consectetur adipiscing elit, sed do eiusmod tempor incididunt ut labore et dolore magna aliqua.</p>
  </div>

  <div class="service" style="left:520px;">
    <div class="service-icon">
      <svg width="22" height="22" viewBox="0 0 22 22"><path d="M3 19 19 3" stroke="#fff" stroke-width="2"/><path d="M15 2v4M13 4h4M6 3v3M4.5 4.5h3M18 12v3M16.5 13.5h3" stroke="#fff" stroke-width="1.3"/></svg>
    </div>
    <h3>COLOR CORRECTION</h3>
    <p>Lorem ipsum dolor sit amet, consectetur adipiscing elit, sed do eiusmod tempor incididunt ut labore et dolore magna aliqua.</p>
  </div>
</section>

<h2 class="section-title" style="top:624px;">Past Projects</h2>
<p class="section-intro" style="top:664px;">Lorem ipsum dolor sit amet, consectetur adipiscing elit, sed do eiusmod tempor incididunt ut labore et dolore magna aliqua. Ut enim ad minim veniam, quis nostrud exercitation ullamco laboris nisi ut aliquip ex ea commodo consequat duis aute irure dolor.</p>

<article class="project" style="left:63px;">
  <div class="project-thumb thumb-warm" role="img" aria-label="Still from a documentary project clip">
    <span class="play"><svg width="10" height="12" viewBox="0 0 10 12"><path d="M1 1l8 5-8 5z" fill="#fff"/></svg></span>
  </div>
  <h4>DUIS AUTE IRURE DOLOR IN</h4>
  <p>Lorem ipsum dolor sit amet, consectetur adipiscing elit, sed do eiusmod tempor.</p>
  <span class="more"><svg width="6" height="6" viewBox="0 0 6 6"><path d="M2 1l2 2-2 2" fill="none" stroke="#d9534f" stroke-width="1.2"/></svg></span>
</article>

<article class="project" style="left:281px;">
  <div class="project-thumb thumb-green" role="img" aria-label="Still from an outdoor interview project clip">
    <span class="play"><svg width="10" height="12" viewBox="0 0 10 12"><path d="M1 1l8 5-8 5z" fill="#fff"/></svg></span>
  </div>
  <h4>DUIS AUTE IRURE DOLOR IN</h4>
  <p>Lorem ipsum dolor sit amet, consectetur adipiscing elit, sed do eiusmod tempor.</p>
  <span class="more"><svg width="6" height="6" viewBox="0 0 6 6"><path d="M2 1l2 2-2 2" fill="none" stroke="#d9534f" stroke-width="1.2"/></svg></span>
</article>

<article class="project" style="left:498px;">
  <div class="project-thumb thumb-blue" role="img" aria-label="Still from a motion graphics title sequence clip">
    <span class="play"><svg width="10" height="12" viewBox="0 0 10 12"><path d="M1 1l8 5-8 5z" fill="#fff"/></svg></span>
  </div>
  <h4>DUIS AUTE IRURE DOLOR IN</h4>
  <p>Lorem ipsum dolor sit amet, consectetur adipiscing elit, sed do eiusmod tempor.</p>
  <span class="more"><svg width="6" height="6" viewBox="0 0 6 6"><path d="M2 1l2 2-2 2" fill="none" stroke="#d9534f" stroke-width="1.2"/></svg></span>
</article>

<div class="divider"></div>

<h2 class="section-title" style="top:966px;">Welcome To Quiet Fern Studios</h2>
<p class="section-intro" style="top:1010px;">Lorem ipsum dolor sit amet, consectetur adipiscing elit, sed do eiusmod tempor incididunt ut labore et dolore magna aliqua. Ut enim ad minim veniam, quis nostrud exercitation ullamco laboris nisi ut aliquip ex ea commodo consequat duis aute irure dolor. Excepteur sint occaecat cupidatat non proident, sunt in culpa qui officia.</p>
<a class="read-more">READ MORE <svg width="5" height="6" viewBox="0 0 5 6"><path d="M1 0.5l3 2.5-3 2.5" fill="none" stroke="#444" stroke-width="1"/></svg></a>

<footer class="footer">
  <div class="footer-col" style="left:63px;"><strong>COPYRIGHT</strong>© 2014 Quiet Fern Studios. All rights reserved.</div>
  <div class="footer-col" style="left:300px;"><strong>ADDRESS</strong>1820 Meadow Lane, Ashford, AF 4021</div>
  <div class="follow"><span class="label">FOLLOW US</span><i></i><i></i><i></i><i></i></div>
</footer>

</body>
</html>
```